Saltbush Creek Plumbing Business card & letter head design

We need a new business card and letter head for our plumbing company called saltbush creek plumbing. attached is the companys logo. We provide domestic and commercial plumbing services in regional western Australia. We are after Something simple yet nice to look at and something that fits within the trade industry.

Target Market(s)

trade/building industry

Contact Information for Business Card

Harlan Mossby
Manager
0481 362 740
enquiries@scplumbingco.net.au
ABN: 47 815 203 966
PCL: 4187

Domestic & Commercial Plumbing
Tip Truck & Excavator hire

Colors

Designer to choose colors to be used in the design.

```html
<!DOCTYPE html>
<html lang="en">
<head>
<meta charset="utf-8">
<title>Saltbush Creek Plumbing – Stationery</title>
<link rel="stylesheet" href="https://fonts.googleapis.com/css2?family=Roboto:wght@400;500;700&display=swap">
<style>
  :root {
    --brand-blue: #0d59a5;
    --ink: #3f3f3f;
    --paper: #ffffff;
    --backdrop: #4b4b4b;
  }
  * { margin: 0; padding: 0; box-sizing: border-box; }
  html, body { width: 1200px; height: 1200px; overflow: hidden; }
  body {
    position: relative;
    background: var(--backdrop);
    font-family: "Roboto", sans-serif;
    color: var(--ink);
  }

  .card, .letterhead { position: absolute; background: var(--paper); }

  /* Brand name block */
  .brand {
    display: flex;
    align-items: center;
    gap: 7px;
    color: var(--brand-blue);
    font-weight: 700;
    line-height: 1.05;
  }
  .brand-mark {
    width: 12px; height: 12px;
    background: var(--brand-blue);
    flex: none;
  }
  .brand-name { font-size: 17px; }

  /* Business card front */
  .card-front { left: 26px; top: 297px; width: 465px; height: 271px; }
  .card-front .brand { position: absolute; left: 60px; top: 118px; }
  .card-divider {
    position: absolute; left: 233px; top: 87px;
    width: 1px; height: 98px; background: var(--ink);
  }
  .contact-block { position: absolute; left: 249px; top: 83px; font-size: 11px; line-height: 15px; }
  .contact-name { font-size: 16px; line-height: 20px; font-weight: 700; color: var(--brand-blue); letter-spacing: 0.2px; }
  .contact-role { margin-bottom: 13px; }
  .card-tagline {
    position: absolute; left: 0; right: 0; bottom: 19px;
    text-align: center; font-size: 11px;
  }

  /* Business card back */
  .card-back { left: 26px; top: 594px; width: 465px; height: 271px; background: var(--brand-blue); }
  .card-back .brand {
    position: absolute; left: 0; right: 0; top: 88px;
    justify-content: center; color: var(--paper); gap: 10px;
  }
  .card-back .brand-mark { width: 18px; height: 18px; background: var(--paper); }
  .card-back .brand-name { font-size: 27px; }
  .card-back .card-tagline { color: var(--paper); }

  /* Letterhead */
  .letterhead { left: 514px; top: 176px; width: 661px; height: 841px; }
  .letterhead .brand { position: absolute; left: 40px; top: 58px; }
  .letterhead-contact {
    position: absolute; right: 42px; top: 50px;
    text-align: right; font-size: 10px; line-height: 12.7px;
  }
</style>
</head>
<body>

  <section class="card card-front">
    <div class="brand">
      <span class="brand-mark"></span>
      <span class="brand-name">Saltbush Creek<br>Plumbing</span>
    </div>
    <div class="card-divider"></div>
    <div class="contact-block">
      <p class="contact-name">HARLAN MOSSBY</p>
      <p class="contact-role">Manager</p>
      <p>0481 362 740</p>
      <p>enquiries@scplumbingco.net.au</p>
      <p>ABN: 47 815 203 966</p>
      <p>PCL: 4187</p>
    </div>
    <p class="card-tagline">Tip Truck &amp; Excavator hire</p>
  </section>

  <section class="card card-back">
    <div class="brand">
      <span class="brand-mark"></span>
      <span class="brand-name">Saltbush Creek<br>Plumbing</span>
    </div>
    <p class="card-tagline">Domestic &amp; Commercial Plumbing</p>
  </section>

  <section class="letterhead">
    <div class="brand">
      <span class="brand-mark"></span>
      <span class="brand-name">Saltbush Creek<br>Plumbing</span>
    </div>
    <div class="letterhead-contact">
      <p>0481 362 740</p>
      <p>enquiries@scplumbingco.net.au</p>
      <p>ABN: 47 815 203 966</p>
      <p>PCL: 4187</p>
    </div>
  </section>

</body>
</html>
```